依頼詳細
12月下旬~1月上旬オープンに向けてのチラシ作成をお願いいたします。オープン以降も同じチラシを定期的にポスティングいたしますので汎用できるようにお願いいたします。
納品はaiデータでお願いいたします。
記載項目
社名や電話番号は後で投稿させていただきます。
サイズ
A4
ページ数
片面
希望イメージ
シンプル 複雑
単色 カラフル
暗い 明るい
日常 高級
遊び心 厳粛
未来的 伝統的
女性的 男性的
希望する色
水色系
納品ファイル
• イラストレーター形式 (.ai)
補足説明
脱毛サロンのロゴを貼り付けさせていただきます。
脱毛器の画像や使用イメージ画像を追加させていただきます。
よろしくお願いいたします。
作成していただいているところに追記すみません。
オープン期間限定キャンペーン→その後、通常価格に戻します。
メニュー内容につきましては
30分→通常3500円
60分→通常4500円
月額会員→通常5500円(初月のみ)
全メニュー1000円off!!
ずーっと会員登録費・事務手数料【無料】
■ 選んだ理由

わかりやすさ。色合い

■ 提案者全員のお礼・コメント

今回たくさんのご応募いただきありがとうございます。
また、どの提案も素敵なもので決めるのに苦慮しました。またよろしくお願いいたします。

```html
<!DOCTYPE html>
<html lang="ja">
<head>
<meta charset="utf-8">
<title>セルフ脱毛サロン mirai オープン</title>
<link rel="stylesheet" href="https://fonts.googleapis.com/css2?family=Shippori+Mincho:wght@500;700;800&family=Noto+Sans+JP:wght@400;500;700&family=Cormorant+Garamond:wght@500&family=Pacifico&display=swap">
<style>
  :root {
    --sky: #7cc4dc;
    --sky-deep: #4aa6c6;
    --sky-pale: #dff1f7;
    --band: #cfe9f2;
    --navy: #1f3550;
    --ink: #3b4a5a;
    --orange: #f08a2e;
    --pink: #e8739a;
    --pink-pale: #fbe1ea;
    --lilac-pale: #f1ebf8;
    --white: #ffffff;
  }
  * { margin: 0; padding: 0; box-sizing: border-box; }
  html, body { width: 845px; height: 1200px; overflow: hidden; background: var(--white); }
  .flyer {
    position: relative; width: 845px; height: 1200px; overflow: hidden;
    background: linear-gradient(180deg, #f6fbfd 0%, #ffffff 55%);
    font-family: "Noto Sans JP", sans-serif; color: var(--ink);
  }
  .hero-photo {
    position: absolute; right: 0; top: 0; width: 450px; height: 700px;
    background: radial-gradient(ellipse at 55% 40%, #f3ddd2 0%, #e9cfc4 30%, #d9e9ef 70%, #eef6f9 100%);
  }
  .tagline {
    position: absolute; left: 40px; top: 42px; line-height: 1.2;
    font-family: "Shippori Mincho", serif; font-weight: 800;
    font-size: 44px; color: var(--navy); letter-spacing: 1px;
  }
  .tagline small { font-size: 32px; }
  .headline {
    position: absolute; left: 34px; top: 108px;
    font-family: "Shippori Mincho", serif; font-weight: 700;
    color: var(--sky); font-size: 156px; line-height: 158px; letter-spacing: -4px;
  }
  .brand {
    position: absolute; left: 40px; top: 590px; display: flex; align-items: center; gap: 18px;
  }
  .brand-mark { width: 74px; height: 74px; border-radius: 50%; border: 3px solid var(--sky); flex: none; }
  .brand-name {
    font-family: "Cormorant Garamond", serif; font-weight: 500;
    font-size: 104px; line-height: 1; color: var(--sky-deep); letter-spacing: 2px;
  }
  .brand-kana {
    font-family: "Shippori Mincho", serif; font-size: 40px; line-height: 1; color: var(--pink); margin-left: 6px;
  }
  .open {
    position: absolute; left: 590px; top: 615px; line-height: 1;
    font-family: "Pacifico", cursive; font-size: 62px; color: var(--orange);
  }
  .info-band {
    position: absolute; left: 0; top: 900px; width: 845px; height: 300px; background: var(--band);
  }
  .features { position: absolute; left: 0; top: 700px; width: 845px; height: 240px; }
  .feature {
    position: absolute; width: 215px; height: 215px; border-radius: 50%;
    display: flex; align-items: center; justify-content: center;
    text-align: center; font-weight: 700; line-height: 1.35;
    box-shadow: 0 4px 10px rgba(60,120,150,0.15);
  }
  .feature p { display: block; }
  .feature--first { left: 20px; top: 15px; background: var(--pink-pale); color: var(--navy); font-size: 28px; }
  .feature--first em { font-style: normal; color: var(--pink); font-size: 31px; }
  .feature--easy { left: 268px; top: 0; background: var(--sky-pale); color: var(--pink); font-size: 34px; }
  .feature--easy small { display: block; font-size: 25px; }
  .feature--kids { left: 560px; top: 15px; background: var(--lilac-pale); color: var(--pink); font-size: 27px; }
  .device-photo {
    position: absolute; left: 0; top: 945px; width: 215px; height: 255px;
    background: linear-gradient(160deg, #f4f7f8 0%, #dfe7ea 60%, #c9d6db 100%);
  }
  .pitch {
    position: absolute; left: 240px; top: 950px; width: 590px;
    font-size: 29px; line-height: 1.45; color: var(--navy); font-weight: 500;
  }
  .footer-brand {
    position: absolute; left: 240px; top: 1045px; display: flex; align-items: center; gap: 10px;
  }
  .footer-brand .brand-mark { width: 34px; height: 34px; border-width: 2px; }
  .footer-brand .brand-name { font-size: 46px; }
  .footer-brand .brand-kana { font-size: 20px; }
  .address { position: absolute; left: 240px; top: 1125px; font-size: 17px; color: var(--navy); letter-spacing: 1px; }
  .map-box {
    position: absolute; left: 585px; top: 1050px; width: 225px; height: 130px;
    background: var(--white); border: 1px solid #9bb8c4;
    font-size: 15px; color: var(--ink); display: flex; align-items: flex-start; justify-content: center; padding-top: 8px;
  }
</style>
</head>
<body>
<main class="flyer">
  <div class="hero-photo" role="img" aria-label="笑顔で頬に手を添える女性の写真"></div>

  <p class="tagline">子供<small>も</small>ムダ毛処理できる</p>
  <h1 class="headline">セルフ<br>脱毛<br>サロン</h1>

  <div class="brand">
    <span class="brand-mark"></span>
    <span class="brand-name">mirai</span>
    <span class="brand-kana">みらい</span>
  </div>
  <p class="open">Open</p>

  <div class="info-band"></div>

  <section class="features">
    <div class="feature feature--first"><p><em>県内初</em>の<br>最新脱毛<br>機器使用</p></div>
    <div class="feature feature--easy"><p>操作簡単<small>安心・安全</small></p></div>
    <div class="feature feature--kids"><p>子供も<br>脱毛ができる<br>機能付</p></div>
  </section>

  <div class="device-photo" role="img" aria-label="脱毛機器と施術イメージの写真"></div>

  <p class="pitch">自分のやりたい所だけ、好きな数だけ、<br>誰にも見られずに脱毛できる。</p>

  <div class="footer-brand">
    <span class="brand-mark"></span>
    <span class="brand-name">mirai</span>
    <span class="brand-kana">みらい</span>
  </div>
  <p class="address">住所：〇〇〇〇〇〇〇〇〇〇〇</p>
  <div class="map-box">地図</div>
</main>
</body>
</html>
```